Upgrade WIX webpage for small family business with kids playground equipment

I am looking for someone to upgrade my established webpage and then add additional features like equipment availability and photos etc.

www.pebbletots.com.au

Looking for a more consistent look. Have attached our price list that I recently had professionally done.

```html
<!DOCTYPE html>
<html lang="en">
<head>
<meta charset="utf-8">
<title>Pebble Tots – Mobile Play Centre</title>
<link rel="stylesheet" href="https://fonts.googleapis.com/css2?family=Passion+One:wght@400;700&family=Bubblegum+Sans&family=Nunito:wght@400;600;700&display=swap">
<style>
:root{
  --red:#e8202a;
  --yellow:#f7c600;
  --green:#8cc63f;
  --green-dark:#6aa22c;
  --forest:#1b3210;
  --cream:#fcf6d6;
  --paper:#fbf8ec;
  --ink:#1a1a1a;
  --navy:#22356b;
  --purple:#9b2d99;
  --white:#ffffff;
}
*{margin:0;padding:0;box-sizing:border-box}
html,body{width:1200px;height:4384px;overflow:hidden}
body{position:relative;background:var(--white);font-family:"Nunito",Arial,sans-serif;color:var(--ink)}
.abs{position:absolute}
.display{font-family:"Passion One",Impact,sans-serif;font-weight:700;letter-spacing:.5px}
.btn{position:absolute;display:flex;align-items:center;justify-content:center;font-family:"Passion One",Impact,sans-serif;font-size:24px;color:var(--ink);background:var(--green);border:2px solid #fff2}
/* header */
.site-header{position:absolute;left:0;top:0;width:1200px;height:83px;background:#fff}
.brand{position:absolute;left:155px;top:10px;display:flex;flex-direction:column}
.brand-name{font-family:"Passion One",Impact,sans-serif;font-size:38px;line-height:36px;color:var(--red);display:flex;align-items:center;gap:10px}
.brand-dot{width:22px;height:22px;border-radius:50%;background:var(--yellow)}
.brand-sub{font-size:12px;font-weight:700;letter-spacing:1.5px;color:#555}
.main-nav{position:absolute;left:495px;top:26px;display:flex;gap:31px;font-family:"Passion One",Impact,sans-serif;font-size:20px;font-weight:400;color:#222}
.main-nav .active{color:var(--red)}
/* hero */
.hero{position:absolute;left:0;top:83px;width:1200px;height:600px}
.hero-photo{position:absolute;inset:0;background:radial-gradient(circle at 75% 45%,#e8b23b 0,#c4402c 28%,#3b5a2a 60%,#1c2416 100%)}
.hero-shade{position:absolute;left:0;top:0;width:620px;height:100%;background:linear-gradient(90deg,rgba(0,0,0,.55),rgba(0,0,0,0))}
.hero-wave{position:absolute;left:0;bottom:0}
.hero-copy{position:absolute;left:157px;top:40px;color:#fff}
.hero-copy .script{font-family:"Bubblegum Sans",cursive;font-size:78px;line-height:78px}
.hero-copy .idea{font-family:"Bubblegum Sans",cursive;font-size:78px;line-height:80px;color:var(--yellow)}
.hero-copy .idea span{color:var(--red)}
.hero-copy .big{font-family:"Passion One",Impact,sans-serif;font-size:86px;line-height:80px}
.hero-copy .sub{font-size:32px;line-height:42px;font-weight:700;margin-top:6px}
/* about */
.about-red{left:160px;top:700px;width:275px;height:275px;border-radius:50%;background:var(--red)}
.about-red-inner{left:205px;top:745px;width:185px;height:185px;border-radius:50%;background:linear-gradient(135deg,#c9a6d8,#7a6a8e)}
.about-photo2{left:262px;top:915px;width:230px;height:230px;border-radius:50%;border:6px solid #111;background:linear-gradient(160deg,#3a9a3a,#e04030 50%,#2860c0)}
.section-title{font-family:"Passion One",Impact,sans-serif;font-size:56px;line-height:56px;color:var(--ink)}
.about-text{left:533px;top:860px;width:515px;font-size:19px;line-height:29.5px;color:#222}
/* packages */
.packages{left:0;top:1187px;width:1200px;height:720px;background:linear-gradient(180deg,#fbf3cf,var(--cream))}
.pkg-card{position:absolute;top:1365px;width:212px;height:365px;background:#fff;border-radius:40px 40px 106px 106px;box-shadow:0 4px 14px rgba(0,0,0,.08);text-align:center}
.pkg-thumb{position:absolute;left:45px;top:-8px;width:135px;height:125px;border:4px solid #ddd;border-radius:6px}
.pkg-name{position:absolute;left:0;right:0;top:135px;font-size:25px;line-height:30px;font-weight:700;color:#222}
.pkg-price{position:absolute;left:0;right:0;top:195px;font-size:28px;font-weight:700;color:var(--red)}
.pkg-btn{position:absolute;left:48px;top:253px;width:116px;height:40px;background:#111;color:#fff;font-family:"Passion One",Impact,sans-serif;font-size:20px;font-weight:400;display:flex;align-items:center;justify-content:center}
/* call band */
.jungle{left:0;top:1900px;width:1200px;height:240px;background:linear-gradient(180deg,var(--cream) 0,#3f8a2a 35%,#2a6a1c 70%,#d9b418 100%)}
.team{left:0;top:2130px;width:1200px;height:600px;background:linear-gradient(180deg,#dcb51a,#e2c21e)}
.team-people{left:150px;top:2250px;width:640px;height:480px;background:linear-gradient(180deg,#c9a27a,#3b5fb4 55%,#1d1d1d);border-radius:200px 200px 0 0}
.call-circle{left:628px;top:2248px;width:414px;height:414px;border-radius:50%;background:var(--red);text-align:center;color:#fff}
/* availability */
.avail{left:0;top:2730px;width:1200px;height:288px;background:var(--green)}
.avail-under{left:157px;top:3018px;width:1043px;height:288px;background:var(--paper)}
.calendar{left:157px;top:2795px;width:465px;height:322px;background:#fff;border:2px solid #222;padding:6px}
.calendar-inner{border:1.5px solid #222;height:100%}
.cal-title{text-align:center;font-size:42px;line-height:44px;font-weight:400;color:#111;border-bottom:1.5px solid #222}
.calendar table{width:100%;border-collapse:collapse;font-size:9px}
.calendar th{font-weight:400;border:1px solid #222;height:12px}
.calendar td{border:1px solid #222;height:47px;vertical-align:top;padding:1px 3px;width:14.28%}
.calendar td.off{color:#aaa}
.badge{top:3135px}
/* follow */
.gallery{left:157px;top:3465px;display:grid;grid-template-columns:repeat(6,135px);grid-auto-rows:128px;gap:16px 16px}
.gallery div{border-radius:2px}
/* footer */
.footer-wave{left:0;top:3770px}
.footer{left:0;top:3850px;width:1200px;height:485px;background:var(--forest);color:#fff}
.foot-brand{left:157px;top:3955px}
.contact-box{position:absolute;left:157px;width:290px;height:68px;display:flex;align-items:center;gap:12px;padding-left:20px;font-size:14px;line-height:19px}
.contact-box strong{font-size:17px;font-weight:400}
.foot-h{font-family:"Passion One",Impact,sans-serif;font-size:24px;font-weight:400}
.foot-list{list-style:none;font-size:14px;line-height:29.5px;color:#e8e8e8;margin-top:8px}
.copyright{left:0;top:4335px;width:1200px;height:49px;background:var(--green);display:flex;align-items:center;justify-content:center;font-size:14px;color:#1a1a1a}
</style>
</head>
<body>

<header class="site-header">
  <div class="brand">
    <div class="brand-name">Pebble Tots<span class="brand-dot"></span></div>
    <div class="brand-sub">MOBILE PLAY CENTRE</div>
  </div>
  <nav class="main-nav"><span class="active">Home</span><span>Packages</span><span>Large games</span><span>About</span><span>Gallery</span><span>Contact</span></nav>
</header>

<section class="hero">
  <div class="hero-photo" role="img" aria-label="Two smiling toddlers playing in a pit full of colourful balls and balloons"></div>
  <div class="hero-shade"></div>
  <div class="hero-copy">
    <div class="script">A Simple</div>
    <div class="idea"><span>IDEA</span> FOR</div>
    <div class="big">ENTERTAIN</div>
    <div class="big">CHILDREN</div>
    <div class="sub">CONTACT OUR FRIENDLY<br>STAFF TODAY</div>
  </div>
  <div class="btn" style="left:158px;top:452px;width:210px;height:46px">CONTACT US NOW</div>
  <svg class="hero-wave" width="1200" height="70" viewBox="0 0 1200 70"><path d="M0 20 C200 60 420 70 640 55 C860 40 1020 20 1200 30 L1200 70 L0 70 Z" fill="#fff"/></svg>
</section>

<svg class="abs" style="left:312px;top:655px" width="36" height="30"><path d="M4 4 L30 8 L12 26 Z" fill="none" stroke="#222" stroke-width="2.5"/></svg>
<svg class="abs" style="left:963px;top:727px" width="44" height="44"><rect x="10" y="10" width="24" height="24" transform="rotate(45 22 22)" fill="none" stroke="#7fb4d8" stroke-width="2"/></svg>
<svg class="abs" style="left:158px;top:1048px" width="46" height="26"><path d="M4 22 A14 14 0 0 1 30 14" fill="none" stroke="#222" stroke-width="3"/></svg>
<svg class="abs" style="left:998px;top:1124px" width="42" height="34"><line x1="4" y1="28" x2="26" y2="6" stroke="#111" stroke-width="4"/><line x1="14" y1="32" x2="38" y2="10" stroke="#ccc" stroke-width="1.5"/></svg>

<div class="abs about-red"></div>
<div class="abs about-red-inner" role="img" aria-label="Child lying inside a soft play tunnel"></div>
<div class="abs about-photo2" role="img" aria-label="Child peeking out from a tower of large building blocks"></div>
<h2 class="abs section-title" style="left:533px;top:785px">ABOUT US</h2>
<p class="abs about-text">Established in September 2016, Pebble Tots Mobile Play Centre is a family owned and operated business based in Riverbend. We service the Sydney Metropolitan area, Wollongong and surrounding areas.</p>
<div class="btn" style="left:533px;top:1026px;width:150px;height:46px">READ MORE</div>

<section class="abs packages" aria-label="Packages"></section>
<h2 class="abs section-title" style="left:0;width:1200px;text-align:center;top:1252px">PACKAGE</h2>

<div class="pkg-card" style="left:155px">
  <div class="pkg-thumb" role="img" aria-label="Colourful climbing frame" style="background:linear-gradient(135deg,#d83a8a,#3a6ad8 50%,#e8d23a)"></div>
  <div class="pkg-name">Mega Mobile<br>Play Centre</div>
  <div class="pkg-price">$790 +GST</div>
  <div class="pkg-btn">CHOOSE IT</div>
</div>
<div class="pkg-card" style="left:382px">
  <div class="pkg-thumb" role="img" aria-label="Indoor play frame with slide" style="background:linear-gradient(135deg,#2a3f8a,#d83030 55%,#e8b52a)"></div>
  <div class="pkg-name">Mobile<br>Play Centre</div>
  <div class="pkg-price">$395 +GST</div>
  <div class="pkg-btn">CHOOSE IT</div>
</div>
<div class="pkg-card" style="left:607px">
  <div class="pkg-thumb" role="img" aria-label="Play gym frame" style="background:linear-gradient(135deg,#e8c23a,#3a8ad8 50%,#d83a3a)"></div>
  <div class="pkg-name">Mobile<br>PLAY GYM</div>
  <div class="pkg-price">$395 +GST</div>
  <div class="pkg-btn">CHOOSE IT</div>
</div>
<div class="pkg-card" style="left:833px">
  <div class="pkg-thumb" role="img" aria-label="Toddler soft play shapes on grass" style="border-color:#3a9a3a;background:linear-gradient(135deg,#3ab0d8,#e03a7a 50%,#e8d23a)"></div>
  <div class="pkg-name">Toddler Soft<br>Play Equip</div>
  <div class="pkg-price">$395 +GST</div>
  <div class="pkg-btn">CHOOSE IT</div>
</div>

<svg class="abs" style="left:557px;top:1759px" width="86" height="38">
  <circle cx="19" cy="19" r="18" fill="#bbb"/><path d="M22 11 L14 19 L22 27" fill="none" stroke="#fff" stroke-width="3"/>
  <circle cx="66" cy="19" r="18" fill="#111"/><path d="M63 11 L71 19 L63 27" fill="none" stroke="#fff" stroke-width="3"/>
</svg>
<div class="btn" style="left:457px;top:1825px;width:285px;height:46px">VIEW ALL PACKAGES</div>

<div class="abs jungle" role="img" aria-label="Band of tropical jungle leaves"></div>
<div class="abs team" role="img" aria-label="Yellow wall with a play centre van in the background"></div>
<div class="abs team-people" role="img" aria-label="Four smiling team members standing together"></div>
<div class="abs call-circle">
  <div class="display" style="font-size:52px;line-height:61px;padding-top:78px;font-weight:400">CALL OUR<br>FRIENDLY STAFF<br>TODAY TO BOOK</div>
</div>
<div class="btn" style="left:760px;top:2537px;width:150px;height:46px">CALL US NOW</div>

<section class="abs avail"></section>
<div class="abs avail-under"></div>
<div class="abs calendar">
  <div class="calendar-inner">
    <div class="cal-title">APRIL 2021</div>
    <table>
      <tr><th>Sunday</th><th>Monday</th><th>Tuesday</th><th>Wednesday</th><th>Thursday</th><th>Friday</th><th>Saturday</th></tr>
      <tr><td class="off">28</td><td class="off">29</td><td class="off">30</td><td class="off">31</td><td>1</td><td>2</td><td>3</td></tr>
      <tr><td>4</td><td>5</td><td>6</td><td>7</td><td>8</td><td>9</td><td>10</td></tr>
      <tr><td>11</td><td>12</td><td>13</td><td>14</td><td>15</td><td>16</td><td>17</td></tr>
      <tr><td>18</td><td>19</td><td>20</td><td>21</td><td>22</td><td>23</td><td>24</td></tr>
      <tr><td>25</td><td>26</td><td>27</td><td>28</td><td>29</td><td>30</td><td class="off">1</td></tr>
    </table>
  </div>
</div>
<h2 class="abs section-title" style="left:657px;top:2808px;font-size:60px;line-height:60px">GET AVAILABILITY</h2>
<p class="abs" style="left:657px;top:2873px;width:360px;font-size:19px;line-height:29.5px">It is a long established fact that a reader will be distracted by the readable content</p>

<svg class="abs badge" style="left:290px" width="76" height="80"><circle cx="38" cy="38" r="36" fill="#2f6fb8"/></svg>
<svg class="abs badge" style="left:502px;top:3143px" width="80" height="80"><circle cx="40" cy="40" r="39" fill="#1d9be3"/></svg>
<svg class="abs badge" style="left:700px" width="66" height="100"><rect x="3" y="3" width="60" height="94" rx="6" fill="#b32a2a"/></svg>
<svg class="abs badge" style="left:913px;top:3145px" width="72" height="72"><rect x="2" y="2" width="68" height="68" rx="6" fill="#5aa83a"/></svg>

<svg class="abs" style="left:156px;top:3366px" width="22" height="22"><circle cx="11" cy="11" r="7" fill="none" stroke="#222" stroke-width="2.5"/></svg>
<svg class="abs" style="left:906px;top:3384px" width="24" height="34"><path d="M6 4 Q16 9 6 14 Q16 19 6 24 Q16 29 6 32" fill="none" stroke="#333" stroke-width="2.5"/></svg>
<div class="abs" style="left:0;width:1200px;top:3377px;display:flex;justify-content:center;align-items:center;gap:12px">
  <svg width="26" height="26"><rect x="3" y="3" width="20" height="20" rx="5" fill="none" stroke="#111" stroke-width="3"/><circle cx="13" cy="13" r="4.5" fill="none" stroke="#111" stroke-width="3"/></svg>
  <h2 class="section-title">FOLLOW US</h2>
</div>
<div class="abs gallery">
  <div role="img" aria-label="Climbing frame" style="background:linear-gradient(135deg,#d83a8a,#3a6ad8)"></div>
  <div role="img" aria-label="Play equipment set up indoors" style="background:linear-gradient(135deg,#c8a27a,#8a3a2a)"></div>
  <div role="img" aria-label="Social feed tile" style="background:#5fa8e0"></div>
  <div role="img" aria-label="Ball pit and soft play" style="background:linear-gradient(135deg,#e8c23a,#3a8ad8)"></div>
  <div role="img" aria-label="Play gym with balls" style="background:linear-gradient(135deg,#e8a23a,#c83a2a)"></div>
  <div role="img" aria-label="Tall play frame" style="background:linear-gradient(135deg,#2a3f8a,#5aa8d8)"></div>
  <div role="img" aria-label="Baby in a ball pit" style="background:linear-gradient(135deg,#e84a3a,#3ab05a)"></div>
  <div role="img" aria-label="Colourful play frame" style="background:linear-gradient(135deg,#7a3ab8,#e8a23a)"></div>
  <div role="img" aria-label="Play frame at an event" style="background:linear-gradient(135deg,#d8c8b0,#b83a2a)"></div>
  <div role="img" aria-label="Soft play area" style="background:linear-gradient(135deg,#3a8ad8,#e8c23a)"></div>
  <div role="img" aria-label="Soft play blocks in a hall" style="background:linear-gradient(135deg,#d8d8d8,#3aa05a)"></div>
  <div role="img" aria-label="Soft play shapes" style="background:linear-gradient(135deg,#3ab0d8,#e03a5a)"></div>
</div>
<svg class="abs" style="left:1115px;top:3742px" width="32" height="16"><path d="M2 4 L8 12 L15 4 L22 12 L29 4" fill="none" stroke="#222" stroke-width="2.5"/></svg>
<svg class="abs" style="left:160px;top:3778px" width="20" height="24"><path d="M14 4 A8 8 0 0 0 14 20" fill="none" stroke="#222" stroke-width="2.5"/></svg>
<svg class="abs" style="left:726px;top:3792px" width="20" height="18"><path d="M10 3 L17 15 L3 15 Z" fill="none" stroke="#666" stroke-width="2"/></svg>

<svg class="abs footer-wave" width="1200" height="82" viewBox="0 0 1200 82"><path d="M0 62 C260 20 520 10 760 30 C960 46 1090 40 1200 20 L1200 82 L0 82 Z" fill="#1b3210"/></svg>
<footer class="abs footer"></footer>

<div class="abs foot-brand brand" style="left:157px;top:3958px">
  <div class="brand-name">Pebble Tots<span class="brand-dot"></span></div>
  <div class="brand-sub" style="color:#bbb">MOBILE PLAY CENTRE</div>
</div>

<div class="contact-box" style="top:4030px;background:var(--yellow);color:#222">
  <svg width="22" height="22"><circle cx="11" cy="11" r="9" fill="none" stroke="#222" stroke-width="1.8"/><path d="M7 6 L9 6 L10 9 L8.5 10 Q10 13 12 13.5 L13 12 L16 13 L16 15 Q10 16 6 8 Z" fill="#222"/></svg>
  <div>Call Us Now<br><strong>0400 218 745</strong></div>
</div>
<div class="contact-box" style="top:4113px;background:var(--navy);color:#fff">
  <svg width="22" height="18"><rect x="1.5" y="2" width="19" height="14" fill="none" stroke="#fff" stroke-width="1.6"/><path d="M2 3 L11 10 L20 3" fill="none" stroke="#fff" stroke-width="1.6"/></svg>
  <div>Send Us A Message<br><strong>sales@pebbletots.com.au</strong></div>
</div>
<div class="contact-box" style="top:4196px;background:var(--purple);color:#fff">
  <svg width="20" height="24"><path d="M10 22 C4 14 2 11 2 8 A8 8 0 0 1 18 8 C18 11 16 14 10 22 Z" fill="none" stroke="#fff" stroke-width="1.6"/><circle cx="10" cy="8" r="3" fill="none" stroke="#fff" stroke-width="1.6"/></svg>
  <div>Visit Us At<br><strong>Riverbend NSW Australia</strong></div>
</div>

<div class="abs" style="left:486px;top:3958px;color:#fff">
  <div class="foot-h">Quick Links</div>
  <ul class="foot-list"><li>Home</li><li>Packages</li><li>Large Games</li><li>About</li><li>Gallery</li><li>Contact</li></ul>
</div>
<div class="abs" style="left:630px;top:3958px;color:#fff">
  <div class="foot-h">Games</div>
  <ul class="foot-list"><li>Four in a Row</li><li>Building Bricks</li><li>Checkers</li><li>Chess</li><li>Chinese Checkers</li><li>Naughts and Crosses</li><li>Quoits</li><li>Kubb</li></ul>
</div>
<div class="abs" style="left:816px;top:3958px;color:#fff;width:230px">
  <div class="foot-h">Get Updates</div>
  <p style="font-size:14px;line-height:21px;margin-top:10px;color:#e8e8e8">To Get Update , Please Join Our Newsletter</p>
</div>
<div class="abs" style="left:818px;top:4073px;width:224px;height:36px;background:#fff;border-radius:18px;display:flex;align-items:center;padding-left:18px;font-size:14px;color:#888">Type Email Address</div>
<div class="abs" style="left:992px;top:4073px;width:50px;height:36px;background:var(--green);border-radius:18px;display:flex;align-items:center;justify-content:center">
  <svg width="18" height="16"><path d="M1 8 L17 1 L12 15 L9 9 Z" fill="#1b3210"/></svg>
</div>
<div class="abs foot-h" style="left:816px;top:4152px;color:#fff">Get Social</div>
<div class="abs" style="left:818px;top:4198px;width:36px;height:36px;background:#2a5bb8"></div>
<div class="abs" style="left:865px;top:4198px;width:36px;height:36px;background:#b8348f"></div>
<div class="abs" style="left:912px;top:4198px;width:36px;height:36px;background:var(--red);display:flex;align-items:center;justify-content:center">
  <svg width="16" height="12"><rect x="1" y="1" width="14" height="10" fill="none" stroke="#fff" stroke-width="1.5"/><path d="M1 1 L8 7 L15 1" fill="none" stroke="#fff" stroke-width="1.5"/></svg>
</div>

<div class="abs copyright">Copyright©2021 pebbletots , All Rights Reserved.</div>

</body>
</html>
```